Webdesign für Personalvermittlung
Zielgruppe
Personalvermittlung
Aufgabenstellung
es soll einladend - nicht zu überladen und natürlich cool und modern sein

```html
<!DOCTYPE html>
<html lang="de">
<head>
<meta charset="utf-8">
<title>carevia job – Personalvermittlung Pflege</title>
<link href="https://fonts.googleapis.com/css2?family=Montserrat:ital,wght@0,400;0,600;0,700;0,800;1,400;1,600&family=Poppins:ital,wght@0,400;0,500;0,600;1,400;1,500&display=swap" rel="stylesheet">
<style>
:root{
  --orange:#f7921e;
  --orange-dark:#f07d10;
  --blue:#29a6e6;
  --blue-light:#e3f3fc;
  --blue-pale:#f1f9fe;
  --navy:#1e2140;
  --text:#2b2b2b;
  --muted:#6f6f6f;
  --line:#3d8fd1;
  --green:#2db34a;
}
*{box-sizing:border-box;margin:0;padding:0}
html,body{width:1200px;height:5168px;overflow:hidden;background:#fff}
body{font-family:"Poppins",sans-serif;color:var(--text);position:relative}
section,header,footer,nav{position:absolute;left:0;width:1200px}
.btn{position:absolute;background:var(--orange);color:#fff;font-family:"Montserrat",sans-serif;font-weight:700;font-size:16px;display:flex;align-items:center;justify-content:center;text-transform:uppercase;border-radius:3px}
.sec-title{position:absolute;left:0;width:1200px;text-align:center;color:var(--orange);font-family:"Montserrat",sans-serif;font-weight:600;font-size:34px;line-height:1.2}
.sec-line{position:absolute;height:2px;background:var(--line)}
.sec-sub{position:absolute;left:0;width:1200px;text-align:center;font-style:italic;font-size:19px;color:#555}

/* header */
.header{top:0;height:108px;background:#fff}
.logo{position:absolute;left:82px;top:14px;display:flex;flex-direction:column;align-items:center}
.logo-mark{width:46px;height:46px;border-radius:50%;background:var(--orange)}
.logo-name{font-weight:600;font-size:18px;color:#333;margin-top:4px}
.topbar{position:absolute;right:84px;top:30px;display:flex;align-items:center;gap:22px;font-size:12px;color:#333}
.topbar .phone{color:var(--blue);display:flex;align-items:center;gap:6px;font-size:13px}
.topbar .apply{background:var(--orange);color:#fff;font-weight:600;font-size:15px;padding:8px 18px;border-radius:3px;display:flex;gap:8px;align-items:center}
.nav{top:108px;height:58px;background:var(--blue)}
.nav a{color:#fff;text-decoration:none;font-family:"Montserrat",sans-serif;font-weight:600;font-size:20px;display:flex;align-items:center;justify-content:center;height:58px;position:absolute;top:0}
.nav .active{background:var(--orange);left:80px;width:156px}

/* hero */
.hero{top:166px;height:734px;overflow:hidden}
.hero-photo{position:absolute;inset:0;background:linear-gradient(100deg,#f4f8fb 0%,#e3edf4 35%,#8db8d7 60%,#5b93c1 80%,#c6d9e6 100%)}
.hero h1{position:absolute;left:102px;top:162px;font-family:"Montserrat",sans-serif;font-weight:800;font-size:44px;line-height:50px;color:#2a2a2a}
.hero h1 span{color:var(--orange);font-size:52px;display:block;margin-top:6px}
.hero p{position:absolute;left:102px;top:352px;font-family:"Montserrat",sans-serif;font-weight:700;font-size:27px;line-height:40px;color:#222}
.hero .btn{left:102px;top:512px;width:230px;height:52px;font-size:15px;border-radius:4px}
.hero .arrow{position:absolute;top:296px}
.dots{position:absolute;left:762px;top:686px;display:flex;gap:12px}
.dots i{width:86px;height:11px;border-radius:6px;background:rgba(255,255,255,.85)}
.dots i.on{background:var(--blue)}
.hero .bubble{position:absolute;left:-90px;top:560px;width:170px;height:170px;border-radius:50%;background:var(--blue);opacity:.5}

/* stats */
.stats{top:900px;height:205px;display:flex;justify-content:center;align-items:center;gap:18px}
.stat{display:flex;align-items:center;gap:10px;color:var(--blue)}
.stat b{font-family:"Montserrat",sans-serif;font-weight:800;font-size:72px}
.stat em{font-size:20px;line-height:28px}
.stat-sep{width:3px;height:80px;background:#ccc}

/* offer */
.offer{top:1105px;height:615px;background:linear-gradient(180deg,#dff0fb,#f7fbfe)}
.offer h2{position:absolute;left:92px;top:26px;color:var(--orange);font-family:"Montserrat",sans-serif;font-weight:600;font-size:35px;line-height:42px}
.offer .sec-line{left:92px;top:193px;width:382px}
.checks{position:absolute;left:96px;top:215px;list-style:none}
.checks li{display:flex;gap:22px;align-items:center;height:54px;font-style:italic;font-size:19px}
.video{position:absolute;left:590px;top:50px;width:525px;height:290px;border-radius:12px;background:linear-gradient(120deg,#1d5aa9 0%,#3f86cf 55%,#c5dbec 100%);overflow:hidden}
.video .play{position:absolute;left:246px;top:110px;width:50px;height:50px;border-radius:50%;border:3px solid #fff;background:rgba(0,0,0,.25)}
.video .bar{position:absolute;left:0;bottom:0;width:100%;height:28px;background:#1a4e93}
.offer .q{position:absolute;left:615px;top:415px;font-style:italic;font-weight:600;font-size:19px;line-height:27px;color:#222}
.offer .btn{left:612px;top:548px;width:242px;height:50px}

/* expect */
.expect{top:1720px;height:980px}
.expect .sec-title{top:50px}
.expect .sec-line{left:292px;top:144px;width:622px}
.expect .sec-sub{top:163px}
.germany{position:absolute;left:380px;top:240px;width:460px;height:620px;background:radial-gradient(ellipse at center,#dcdcdc 0%,#e6e6e6 60%,rgba(255,255,255,0) 72%)}
.feat{position:absolute;width:320px}
.feat h3{color:var(--orange);font-family:"Montserrat",sans-serif;font-weight:600;font-size:23px;line-height:34px;margin-left:75px;width:235px}
.feat p{margin:18px 0 0 75px;width:240px;font-size:14px;line-height:26px;color:#666}
.feat p b{color:var(--orange)}
.feat svg{position:absolute;left:0;top:0}

/* about */
.about{top:2700px;height:415px;background:linear-gradient(180deg,#d3ebfa,#ecf7fd)}
.about .sec-title{top:50px}
.about .sec-line{left:278px;top:104px;width:622px}
.about .sec-sub{top:124px}
.about p{position:absolute;left:150px;width:900px;top:182px;text-align:center;font-style:italic;font-size:14.5px;line-height:26px;color:#444}
.about .btn{left:500px;top:318px;width:204px;height:52px}

/* reviews */
.reviews{top:3115px;height:605px;overflow:hidden}
.reviews .sec-title{top:52px}
.reviews .sec-line{left:298px;top:110px;width:622px}
.reviews .sec-sub{top:128px;line-height:28px;left:300px;width:620px}
.card{position:absolute;background:#fff;border-radius:10px;box-shadow:0 3px 12px rgba(0,0,0,.12);text-align:center;font-size:13.5px;line-height:22px;color:#333}
.card .quote{font-family:"Montserrat",sans-serif;font-weight:800;font-size:70px;color:var(--orange);line-height:60px;height:40px}
.card .person{display:flex;align-items:center;gap:14px;text-align:left}
.card .avatar{width:92px;height:92px;border-radius:50%;background:linear-gradient(135deg,#c9d6e0,#7c96ad);flex:none}
.card .person b{font-weight:600;font-size:16px}
.nav-circle{position:absolute;width:46px;height:46px;border-radius:50%;background:#fff;box-shadow:0 2px 6px rgba(0,0,0,.18);display:flex;align-items:center;justify-content:center}

/* contact */
.contact{top:3720px;height:710px}
.form h2{position:absolute;left:108px;top:58px;color:var(--orange);font-family:"Montserrat",sans-serif;font-weight:600;font-size:32px;line-height:38px}
.form .hint{position:absolute;left:108px;top:158px;font-style:italic;font-size:14px;color:#777}
.form .sep{position:absolute;left:108px;top:185px;width:552px;height:1px;background:#ddd}
.form label{position:absolute;font-size:13px;color:#333}
.form .field{position:absolute;border:1px solid #ddd;background:#fff;font-style:italic;font-size:12px;color:#999;padding:14px 14px}
.form .field.active{border:2px solid #8ab4d8}
.form .btn{left:108px;top:591px;width:553px;height:50px;font-size:16px}
.panel{position:absolute;left:700px;top:15px;width:500px;height:660px;background:linear-gradient(180deg,#dff0fb,#eef8fe);overflow:hidden}
.panel h2{position:absolute;left:16px;top:38px;color:var(--orange);font-family:"Montserrat",sans-serif;font-weight:600;font-size:33px}
.panel h4{position:absolute;left:16px;font-style:italic;font-weight:400;font-size:26px;color:#444}
.panel .portrait{position:absolute;left:20px;top:132px;width:112px;height:130px;border-radius:50%;background:linear-gradient(160deg,#e8eef3,#6f8193)}
.panel .name{position:absolute;left:24px;top:290px;font-style:italic;font-weight:600;font-size:26px;color:#222}
.info{position:absolute;left:26px;display:flex;gap:16px;align-items:flex-start;font-style:italic;font-weight:600;font-size:17px;color:#222;line-height:22px}
.info u{text-decoration:underline}
.panel .blob{position:absolute;right:-50px;bottom:-60px;width:150px;height:150px;border-radius:50%;background:var(--orange)}

/* map */
.map{top:4430px;height:450px;background:linear-gradient(135deg,#eef1f3,#e3e8ec 50%,#dfe6d9)}

/* footer */
.footer{top:4880px;height:232px;width:1186px;background:var(--navy);color:#dfe1ef}
.f-logo{position:absolute;left:98px;top:34px;display:flex;flex-direction:column;align-items:center}
.f-logo .mark{width:76px;height:76px;border-radius:50%;background:var(--orange)}
.f-logo .name{font-weight:600;font-size:26px;color:#fff;margin-top:6px}
.socials{display:flex;gap:12px;margin-top:10px}
.socials i{width:22px;height:22px;background:#fff;border-radius:3px}
.f-col h5{position:absolute;font-style:italic;font-weight:400;font-size:19px;color:#dfe1ef}
.f-col .rule{position:absolute;height:1px;background:#555a7a}
.f-links{position:absolute;left:440px;top:110px;list-style:disc;font-style:italic;font-size:12px;line-height:20px}
.subscribe{position:absolute;left:788px;top:66px;width:330px;height:48px;background:#fff;border-radius:2px;font-style:italic;font-size:12px;color:#999;display:flex;align-items:center;gap:18px;padding-left:14px}
.f-note{position:absolute;left:788px;top:132px;width:320px;font-style:italic;font-size:12px;line-height:17px}
.copy{position:absolute;top:5124px;left:0;width:1200px;text-align:center;font-size:13px;color:#333}
</style>
</head>
<body>

<header class="header">
  <div class="logo"><span class="logo-mark"></span><span class="logo-name">carevia job</span></div>
  <div class="topbar">
    <span>Any Qirgendeine Frage</span>
    <span class="phone"><svg width="14" height="14" viewBox="0 0 24 24"><path fill="#29a6e6" d="M6.6 10.8a15.1 15.1 0 0 0 6.6 6.6l2.2-2.2c.3-.3.7-.4 1-.2 1.1.4 2.3.6 3.6.6.6 0 1 .4 1 1V20c0 .6-.4 1-1 1A17 17 0 0 1 3 4c0-.6.4-1 1-1h3.5c.6 0 1 .4 1 1 0 1.3.2 2.5.6 3.6.1.3 0 .7-.2 1z"/></svg>07000 123 456 7</span>
    <span class="apply"><svg width="14" height="14" viewBox="0 0 24 24"><path fill="#fff" d="M3 17.2V21h3.8l11-11-3.8-3.8zM20.7 7a1 1 0 0 0 0-1.4l-2.3-2.3a1 1 0 0 0-1.4 0l-1.8 1.8 3.8 3.8z"/></svg>ANWENDEN</span>
  </div>
</header>

<nav class="nav">
  <a class="active">Home</a>
  <a style="left:290px">Wir Bieten Dir</a>
  <a style="left:540px">Uber Uns</a>
  <a style="left:762px">Kontakt</a>
</nav>

<section class="hero">
  <div class="hero-photo" role="img" aria-label="Foto: Pflegekräfte in blauer Berufskleidung mit Stethoskop"></div>
  <div class="bubble"></div>
  <h1>DEIN NÄCHSTER<br>KARRIERESCHRITT IM<span>PFLEGEBERUF!</span></h1>
  <p>Wir bieten Ihnen den perfekten<br>Job als Führungskraft!</p>
  <div class="btn">ICH WILL EIN ANGEBOT!</div>
  <svg class="arrow" style="left:58px" width="20" height="36" viewBox="0 0 20 36"><path d="M17 2 3 18l14 16" stroke="#fff" stroke-width="3" fill="none"/></svg>
  <svg class="arrow" style="left:1130px" width="20" height="36" viewBox="0 0 20 36"><path d="M3 2l14 16L3 34" stroke="#fff" stroke-width="3" fill="none"/></svg>
  <div class="dots"><i></i><i class="on"></i><i></i><i></i></div>
</section>

<section class="stats">
  <div class="stat"><b>15</b><em>Jahren<br>Erfahrung</em></div>
  <div class="stat-sep"></div>
  <div class="stat"><b>100+</b><em>Mitglied</em></div>
  <div class="stat-sep"></div>
  <div class="stat"><b>10+</b><em>Arbeitsplatz</em></div>
</section>

<section class="offer">
  <h2>Wir bieten Ihnen<br>den perfekten<br>Job als Führungskraft!</h2>
  <div class="sec-line"></div>
  <ul class="checks">
    <li><svg width="24" height="18" viewBox="0 0 24 18"><path d="M2 9l7 7L22 2" stroke="#2db34a" stroke-width="4" fill="none"/></svg>Wohnbereichsleiter/in</li>
    <li><svg width="24" height="18" viewBox="0 0 24 18"><path d="M2 9l7 7L22 2" stroke="#2db34a" stroke-width="4" fill="none"/></svg>Pflegedienstleiter/in</li>
    <li><svg width="24" height="18" viewBox="0 0 24 18"><path d="M2 9l7 7L22 2" stroke="#2db34a" stroke-width="4" fill="none"/></svg>Stationsleiter/in</li>
    <li><svg width="24" height="18" viewBox="0 0 24 18"><path d="M2 9l7 7L22 2" stroke="#2db34a" stroke-width="4" fill="none"/></svg>OP-Manager/in</li>
    <li><svg width="24" height="18" viewBox="0 0 24 18"><path d="M2 9l7 7L22 2" stroke="#2db34a" stroke-width="4" fill="none"/></svg>Heimleiter/in</li>
    <li><svg width="24" height="18" viewBox="0 0 24 18"><path d="M2 9l7 7L22 2" stroke="#2db34a" stroke-width="4" fill="none"/></svg>Klinikdirektor/in</li>
  </ul>
  <div class="video" role="img" aria-label="Vorschaubild eines Willkommensvideos mit Ärzten im Klinikflur"><span class="bar"></span><span class="play"></span></div>
  <div class="q">und willst Dich verändern? Oder möchtest eine<br>Weiterbildung in die Management-Ebene?<br><br>Dann nimm Kontakt zu uns auf...</div>
  <div class="btn">WIR BIETEN DIR</div>
</section>

<section class="expect">
  <div class="sec-title">Was darfst Du von<br>CAREVIA-JOB.de erwarten?</div>
  <div class="sec-line"></div>
  <div class="sec-sub">Ihr Erfolg, unser Engagement</div>
  <div class="germany" role="img" aria-label="Dezente Landkarte von Deutschland im Hintergrund"></div>

  <div class="feat" style="left:100px;top:230px">
    <svg width="46" height="40" viewBox="0 0 46 40"><rect x="2" y="10" width="42" height="28" rx="4" fill="#f7921e"/><rect x="15" y="3" width="16" height="9" rx="2" fill="none" stroke="#f7921e" stroke-width="3"/></svg>
    <h3>Zugriff auf mehr Stellen</h3>
    <p>In Zusammenarbeit mit Einrichtungen und Kliniken erhalten unsere Kandidaten einen zugesicherten Bonus in Höhe von 750 EUR für das Vertrauen bei Ihrem Jobwechsel in carevia-Job.de</p>
  </div>
  <div class="feat" style="left:440px;top:230px">
    <svg width="50" height="30" viewBox="0 0 50 30"><path d="M2 4h34l10 10-10 10H2z" fill="#f7921e"/></svg>
    <h3>100% kostenfrei</h3>
    <p>Unsere Dienstleistung ist für Dich als Bewerber 100% kostenfrei! Es gibt auch garantiert keine versteckten Kosten!</p>
  </div>
  <div class="feat" style="left:785px;top:230px">
    <svg width="48" height="24" viewBox="0 0 48 24"><path d="M24 12c-5-7-18-9-18 0s13 7 18 0 18-9 18 0-13 7-18 0z" stroke="#f7921e" stroke-width="4" fill="none"/></svg>
    <h3>Dauerhafte Betreuung</h3>
    <p>Dein neuer Arbeitgeber hält nicht was er verspricht? Keine Sorge, wir werden für Dich sofort wieder aktiv und bieten Dir schnell neue Möglichkeiten an - ohne dass Du erneut Bewerbungen versenden musst! Ein Anruf oder eine Email genügt!</p>
  </div>
  <div class="feat" style="left:100px;top:590px">
    <svg width="36" height="44" viewBox="0 0 36 44"><path d="M3 3h22l8 8v30H3z" fill="none" stroke="#f7921e" stroke-width="3"/><path d="M9 18h16M9 25h16M9 32h10" stroke="#f7921e" stroke-width="2.5"/></svg>
    <h3 style="width:180px">Alle Versprechungen findest Du im Arbeitsvertrag</h3>
    <p>In Zusammenarbeit mit Einrichtungen und Kliniken erhalten unsere Kandidaten einen zugesicherten Bonus in Höhe von 750 EUR für das Vertrauen bei Ihrem Jobwechsel in carevia-Job.de</p>
  </div>
  <div class="feat" style="left:440px;top:590px">
    <svg width="48" height="34" viewBox="0 0 48 34"><path d="M3 17C12 4 36 4 45 17 36 30 12 30 3 17z" fill="none" stroke="#f7921e" stroke-width="4"/><path d="M8 2l32 30" stroke="#f7921e" stroke-width="4"/></svg>
    <h3>Anonymität</h3>
    <p>Wir erstellen ein Profil Deiner Kenntnisse und Fähigkeiten sowie Deiner Berufserfahrung. Weder Dein Name, noch Deine Vorarbeitgeber tauchen im ersten Schritt auf. Erst wenn eine Einrichtung oder Klinik daran Interesse zeigt, entscheiden wir gemeinsam, wie es weitergeht!</p>
  </div>
  <div class="feat" style="left:785px;top:590px">
    <svg width="40" height="40" viewBox="0 0 40 40"><circle cx="20" cy="14" r="10" fill="#f7921e"/><path d="M4 38c2-10 8-14 16-14s14 4 16 14z" fill="#f7921e"/></svg>
    <h3>Keine Zeitarbeit</h3>
    <p>Wir vermitteln ausschließlich in Festanstellungen direkt bei Kliniken oder Einrichtungen. Wir können Dir jedoch wertvolle Tipps geben , sollte Zeitarbeit für Dich in Frage kommen ... <b>WIR KENNEN UNS AUS!</b></p>
  </div>
</section>

<section class="about">
  <div class="sec-title">ÜBER UNS</div>
  <div class="sec-line"></div>
  <div class="sec-sub">Ihr Erfolg, unser Engagement</div>
  <p>CAREVIA-JOB.de hat es sich mit über 15 Jahren Erfahrung zum Ziel gesetzt, Fachkräften im Gesundheitswesen dabei zu helfen, lohnende Führungspositionen zu finden. Wir sind darauf spezialisiert, qualifizierte Kandidaten mit erstklassigen Gesundheitseinrichtungen zusammenzubringen.</p>
  <div class="btn">WEITER</div>
</section>

<section class="reviews">
  <div class="sec-title">BEWERBERERFAHRUNG</div>
  <div class="sec-line"></div>
  <div class="sec-sub">Bewerber haben Folgendes bei uns erlebt und ihre Erfahrungen geschildert</div>

  <div class="card" style="left:-130px;top:225px;width:460px;height:280px;padding:20px 30px 0 130px;text-align:left">
    <div class="quote" style="text-align:left;padding-left:30px">&rdquo;</div>
    <div style="text-align:center">Lorem Ipsum<br>"Neque Porro Quisquam Est Qui Dolorem Ipsum Quia Dolor Sit Amet, Consectetur, Adipisci Velit..."<br>"There Is No One Who Loves Pain Itself, Who Seeks After It And Wants To Have It, Simply Because It Is Pain..."</div>
    <div style="margin-top:28px;font-size:16px"><b style="font-weight:600">Lukas Hartmann</b><br>Mitglied CAREVIA-JOB</div>
  </div>

  <div class="card" style="left:968px;top:225px;width:420px;height:275px;padding:20px 20px 0 20px">
    <div class="quote" style="text-align:right;padding-right:210px">&rdquo;</div>
    <div style="text-align:left;padding-left:10px">Lorem Ipsum<br>"Neque Porro Quisquam Est Qui Dolorem<br>"There Is No One Who Loves Pain Itself<br>Wants To Have It, Simply</div>
    <div class="person" style="margin-top:22px"><span class="avatar" role="img" aria-label="Porträtfoto eines Bewerbers"></span><span><b>Lukas Hartmann</b><br>Mitglied CAREVIA-JOB</span></div>
  </div>

  <div class="card" style="left:395px;top:245px;width:480px;height:270px;padding:10px 26px 0">
    <div class="quote">&rdquo;</div>
    <div>Lorem Ipsum<br>"Neque Porro Quisquam Est Qui Dolorem Ipsum Quia Dolor Sit Amet, Consectetur, Adipisci Velit..."<br>"There Is No One Who Loves Pain Itself, Who Seeks After It And Wants To Have It, Simply Because It Is Pain..."</div>
    <div class="person" style="margin-top:14px"><span class="avatar" role="img" aria-label="Porträtfoto eines Bewerbers"></span><span><b>Jonas Berger</b><br>Mitglied CAREVIA-JOB</span></div>
  </div>
  <div class="nav-circle" style="left:368px;top:380px"><svg width="14" height="20" viewBox="0 0 14 20"><path d="M11 2 3 10l8 8" stroke="#f7921e" stroke-width="3" fill="none"/></svg></div>
  <div class="nav-circle" style="left:852px;top:380px"><svg width="14" height="20" viewBox="0 0 14 20"><path d="M3 2l8 8-8 8" stroke="#f7921e" stroke-width="3" fill="none"/></svg></div>
</section>

<section class="contact">
  <div class="form">
    <h2>Nimm ganz einfach Kontakt zu uns<br>auf:</h2>
    <div class="hint">gewünschter Rückruf-Zeitpunkt</div>
    <div class="sep"></div>
    <label style="left:108px;top:220px">Nachname</label>
    <div class="field" style="left:108px;top:245px;width:264px;height:46px">Gib deinen Namen ein</div>
    <label style="left:398px;top:220px">E-Mail-Adresse</label>
    <div class="field active" style="left:398px;top:245px;width:264px;height:46px">John.exp@gml</div>
    <label style="left:108px;top:305px">Betreff</label>
    <div class="field" style="left:108px;top:330px;width:554px;height:72px">Geben Sie Ihre Anforderung ein...</div>
    <label style="left:108px;top:418px">Nachricht</label>
    <div class="field" style="left:108px;top:443px;width:554px;height:72px">Was möchten Sie vermitteln?</div>
    <div class="btn">SENDEN</div>
  </div>

  <div class="panel">
    <h2>KONTAKTDATEN</h2>
    <h4 style="top:88px">Ansprechpartner</h4>
    <div class="portrait" role="img" aria-label="Porträtfoto des Ansprechpartners im Anzug"></div>
    <div class="name">Herr Martin Kessler</div>
    <div class="info" style="top:343px"><svg width="20" height="20" viewBox="0 0 24 24"><path fill="#f7921e" d="M6.6 10.8a15.1 15.1 0 0 0 6.6 6.6l2.2-2.2c.3-.3.7-.4 1-.2 1.1.4 2.3.6 3.6.6.6 0 1 .4 1 1V20c0 .6-.4 1-1 1A17 17 0 0 1 3 4c0-.6.4-1 1-1h3.5c.6 0 1 .4 1 1 0 1.3.2 2.5.6 3.6.1.3 0 .7-.2 1z"/></svg>07000 123 456 7</div>
    <div class="info" style="top:392px"><svg width="20" height="16" viewBox="0 0 20 16"><rect x="1" y="1" width="18" height="14" rx="2" fill="#f7921e"/><path d="M2 3l8 6 8-6" stroke="#fff" stroke-width="2" fill="none"/></svg><u>martin.kessler@carevia-job.de</u></div>
    <h4 style="top:436px">Adresse:</h4>
    <div class="info" style="top:493px"><svg width="22" height="22" viewBox="0 0 22 22"><rect x="2" y="6" width="8" height="14" fill="#f7921e"/><rect x="12" y="2" width="8" height="18" fill="#f7921e"/></svg>Musterpark 12, 10115<br>Musterstadt</div>
    <div class="info" style="top:555px"><svg width="20" height="20" viewBox="0 0 24 24"><path fill="#f7921e" d="M6.6 10.8a15.1 15.1 0 0 0 6.6 6.6l2.2-2.2c.3-.3.7-.4 1-.2 1.1.4 2.3.6 3.6.6.6 0 1 .4 1 1V20c0 .6-.4 1-1 1A17 17 0 0 1 3 4c0-.6.4-1 1-1h3.5c.6 0 1 .4 1 1 0 1.3.2 2.5.6 3.6.1.3 0 .7-.2 1z"/></svg>07000 123 456 7</div>
    <div class="info" style="top:604px"><svg width="20" height="16" viewBox="0 0 20 16"><rect x="1" y="1" width="18" height="14" rx="2" fill="#f7921e"/><path d="M2 3l8 6 8-6" stroke="#fff" stroke-width="2" fill="none"/></svg><u>info@carevia-job.de</u></div>
    <div class="blob"></div>
  </div>
</section>

<section class="map" role="img" aria-label="Stadtplan mit Standortmarkierung des Büros"></section>

<footer class="footer">
  <div class="f-logo"><span class="mark"></span><span class="name">carevia job</span><div class="socials"><i></i><i></i><i></i><i></i></div></div>
  <div class="f-col">
    <h5 style="left:420px;top:28px">Seitenverzeichnis</h5>
    <div class="rule" style="left:420px;top:62px;width:320px"></div>
    <ul class="f-links"><li>HOME</li><li>WIR BIETEN DIR</li><li>ÜBER UNS</li><li>KONTAKT</li></ul>
    <h5 style="left:788px;top:28px">Abonnieren</h5>
    <div class="rule" style="left:788px;top:56px;width:330px"></div>
    <div class="subscribe"><svg width="18" height="14" viewBox="0 0 20 16"><rect x="1" y="1" width="18" height="14" rx="2" fill="none" stroke="#f7921e" stroke-width="1.5"/><path d="M2 3l8 6 8-6" stroke="#f7921e" stroke-width="1.5" fill="none"/></svg>Geben sie ihre E-Mail Adresse ein</div>
    <div class="f-note">Senden Sie eine E-Mail und Sie erhalten regelmäßig unsere Newsletter, Service-Blogs und Pressemitteilungen</div>
  </div>
</footer>
<div class="copy">Copyright 2024 carevia-job.de, All Right Reserved</div>

</body>
</html>
```